Party Invitation for Newly Weds

We would like a A5 flyer-style invite in a file suitable for both hard-copy print and web-publishing. It should be designed in the style of a 1950's American Diner Menu incorporating the colours: Ivory, Crimson, Black, and possibly period Green.

We think using the shape of a 50's Juke Box could be a good platform for the design although we are very open to other ideas. We require the design to include the following features:

1. A tattoo-style heart with scroll banner containing our names - TED & LUCY

2. Main Heading - "Wedlock Wing-Ding & Nuptial Knees Up"

3. Feature Headings with icons - DRINK (with cocktail glasses), DANCE (with twisting silhouettes), DEVOUR (with burger & fries)

4. Sub Headings as Menu Items with descriptions as follows:

a. Hey Cat, When's It At?
Venue Doors @ 7pm
Bride & Groom Arrive @ 7.30pm
Be there or be sQuare!

b. Where To Go, Daddy-O!
The Millpond
7, Brackwell Lane
Leeds, LS2 9QT

c. What's Cookin', Man?
DJs & Dancing all night from 7pm
Food Served on the terrace from 8pm
Late Bar from til 2am

d. Ya need digs? Dig this...
Special Rate for Party Guests at Marlow Quayside
£79 Bed & Breakfast
Limited Numbers - Book Early
Call (0113) 2987654 and quote 'PEXOR'

e. If You Want To Share Your Good Vibes...
Your presence, your love and your laughter will be a real neat-o gift for us to cherish, but should you want to splash the cash and spread your love we would be MADE UP with a small donation towards our American Road Trip Honeymoon!!

f. Please R.S.V.P by July 1st.

g. Strictly Over 18's Only

Industry/Entity Type

Publishing

Colors
87cfc6
f04b51
fefdec
1b1b1b

Requirements
Must have
• see project description
• genuine late 50's/early 60's retro style
• classic fonts
Nice to have
• asymmetric shapes
• personal touches
Should not have
• over dependence on food imagery - this is a menu-style design, not an actual menu!

```html
<!DOCTYPE html>
<html lang="en">
<head>
<meta charset="utf-8">
<title>Wedlock Wing-Ding &amp; Nuptial Knees Up – Ted &amp; Lucy</title>
<link rel="stylesheet" href="https://fonts.googleapis.com/css2?family=Fontdiner+Swanky&family=Lobster&family=Lobster+Two:ital,wght@1,700&family=Special+Elite&family=Bevan&display=swap">
<style>
  :root {
    --teal: #87cfc6;
    --teal-deep: #5fb7ad;
    --crimson: #f04b51;
    --crimson-dark: #b8262d;
    --ivory: #fefdec;
    --ink: #1b1b1b;
    --gold: #f7d35c;
  }
  * { margin: 0; padding: 0; box-sizing: border-box; }
  html, body { width: 847px; height: 1200px; overflow: hidden; }
  body {
    position: relative;
    background: radial-gradient(ellipse at 50% 40%, var(--teal) 0%, var(--teal-deep) 100%);
    font-family: "Special Elite", "Courier New", monospace;
    color: var(--ink);
  }
  .jukebox-frame { position: absolute; left: 0; top: 0; }
  .heart-emblem {
    position: absolute; left: 250px; top: 80px; width: 347px; height: 250px;
    border-radius: 50% 50% 46% 46% / 55% 55% 45% 45%;
    background: radial-gradient(circle at 50% 45%, var(--crimson) 0%, var(--crimson-dark) 70%, #8a1c22 100%);
    border: 3px solid var(--ink);
  }
  .names-scroll {
    position: absolute; left: 300px; top: 180px; width: 247px;
    text-align: center;
    font-family: "Lobster", cursive; font-size: 30px; color: var(--crimson-dark);
    background: var(--ivory); border: 3px solid var(--ink); border-radius: 6px;
    padding: 2px 0 4px; transform: rotate(-6deg);
  }
  .title-band { position: absolute; left: 125px; top: 345px; width: 597px; text-align: center; }
  .title-band .stripe { height: 8px; background: var(--crimson); border-top: 2px solid var(--ink); border-bottom: 2px solid var(--ink); margin: 0 20px; }
  .main-title {
    font-family: "Fontdiner Swanky", serif; color: var(--crimson-dark);
    font-size: 33px; line-height: 40px; padding: 8px 0 6px;
  }
  .features {
    position: absolute; left: 140px; top: 458px; width: 567px;
    display: flex; justify-content: space-between; align-items: center;
  }
  .feature { display: flex; align-items: center; gap: 8px; }
  .feature-label { font-family: "Bevan", serif; color: var(--crimson); font-size: 22px; letter-spacing: 3px; }
  .feature-icon { width: 62px; height: 70px; border-radius: 10px; }
  .icon-drink { background: linear-gradient(160deg, var(--crimson) 0%, #c9d8d3 100%); }
  .icon-dance { background: linear-gradient(160deg, var(--ink) 0%, var(--crimson) 100%); }
  .icon-devour { background: linear-gradient(160deg, #d88a3a 0%, var(--crimson) 100%); }
  .feature-dance { flex-direction: column; gap: 2px; }
  .menu {
    position: absolute; left: 140px; top: 555px; width: 567px; height: 405px;
    display: flex;
  }
  .menu-col { width: 50%; padding: 0 14px; }
  .menu-col + .menu-col { border-left: 3px solid var(--ink); }
  .menu-item { margin-bottom: 20px; }
  .menu-heading { font-family: "Lobster Two", cursive; font-weight: 700; font-style: italic; font-size: 24px; line-height: 27px; margin-bottom: 4px; }
  .menu-text { font-size: 16px; line-height: 21px; }
  .small-print { font-size: 12px; line-height: 16px; }
  .notes { margin-top: 16px; font-size: 13px; line-height: 19px; color: var(--crimson-dark); }
  .gift-banner {
    position: absolute; left: 55px; top: 975px; width: 737px; height: 112px;
    background: var(--crimson); border: 3px solid var(--ink);
    text-align: center; padding: 8px 40px 0;
  }
  .gift-heading { font-family: "Lobster", cursive; color: var(--gold); font-size: 25px; text-shadow: 2px 2px 0 var(--ink); }
  .gift-text { color: var(--ivory); font-size: 13.5px; line-height: 17px; margin-top: 4px; }
</style>
</head>
<body>
  <svg class="jukebox-frame" width="847" height="1200" viewBox="0 0 847 1200" aria-hidden="true">
    <path d="M95 1140 L95 360 C95 150 250 28 423 28 C596 28 752 150 752 360 L752 1140 Z" fill="var(--crimson)" stroke="var(--ink)" stroke-width="4"/>
    <path d="M125 1000 L125 370 C125 178 265 62 423 62 C581 62 722 178 722 370 L722 1000 Z" fill="var(--ivory)" stroke="var(--ink)" stroke-width="3"/>
    <rect x="80" y="1135" width="687" height="22" fill="var(--ink)"/>
  </svg>

  <div class="heart-emblem" role="img" aria-label="Tattoo-style red heart pierced by an arrow, wrapped in a scroll banner"></div>
  <div class="names-scroll">Ted &amp; Lucy</div>

  <header class="title-band">
    <div class="stripe"></div>
    <h1 class="main-title">Wedlock Wing-Ding<br>&amp; Nuptial Knees Up</h1>
    <div class="stripe"></div>
  </header>

  <section class="features">
    <div class="feature">
      <div class="feature-icon icon-drink" role="img" aria-label="Cocktail glass icon"></div>
      <span class="feature-label">Drink</span>
    </div>
    <div class="feature feature-dance">
      <div class="feature-icon icon-dance" role="img" aria-label="Twisting dancer silhouettes"></div>
      <span class="feature-label">Dance</span>
    </div>
    <div class="feature">
      <span class="feature-label">Devour</span>
      <div class="feature-icon icon-devour" role="img" aria-label="Burger and fries icon"></div>
    </div>
  </section>

  <main class="menu">
    <div class="menu-col">
      <div class="menu-item">
        <h2 class="menu-heading">Hey Cat,<br>When's It At?</h2>
        <p class="menu-text">Venue Doors @ 7pm<br>Bride &amp; Groom Arrive @ 7.30pm<br>Be there or be sQuare!</p>
      </div>
      <div class="menu-item">
        <h2 class="menu-heading">Where To Go,<br>Daddy-O!</h2>
        <p class="menu-text">The Millpond<br>7, Brackwell Lane<br>Leeds, LS2 9QT</p>
      </div>
      <p class="notes">* Please R.S.V.P by July 1st.<br>* Strictly Over 18's Only</p>
    </div>
    <div class="menu-col">
      <div class="menu-item">
        <h2 class="menu-heading">What's Cookin',<br>Man?</h2>
        <p class="menu-text">DJs &amp; Dancing all night from 7pm.<br>Food Served on the Terrace from 8pm.<br>Late Bar til 2am.</p>
      </div>
      <div class="menu-item">
        <h2 class="menu-heading">Ya need digs?<br>Dig this...</h2>
        <p class="menu-text">Special Rate for Party Guests at<br>Marlow Quayside<br>£79 Bed &amp; Breakfast</p>
        <p class="small-print">Limited Numbers - Book Early<br>Call (0113) 2987654<br>and quote 'PEXOR'</p>
      </div>
    </div>
  </main>

  <footer class="gift-banner">
    <h2 class="gift-heading">If You Want To Share Your Good Vibes...</h2>
    <p class="gift-text">Your presence, your love and your laughter will be a real neat-o gift for us to cherish, but should you want to splash the cash and spread your love we would be MADE UP with a small donation towards our American Road Trip Honeymoon!!</p>
  </footer>
</body>
</html>
```